Quarry Pharmacy Agents Business Card

Hi Desmond - thank you for the Logo - I'm very happy with it.

Can you please design a business card for me using the logo we've decided on.
Updates

Phone Number is (03) 8417 3061 Fax Number is (03) 8417 3062 Please update on the business card Thank you

Industry/Entity Type

Business

```html
<!DOCTYPE html>
<html lang="en">
<head>
<meta charset="utf-8">
<title>Quarry Pharmacy Agents – Business Card</title>
<link rel="stylesheet" href="https://fonts.googleapis.com/css2?family=Montserrat:wght@400;500;700&display=swap">
<style>
  :root {
    --ink: #111111;
    --paper: #ffffff;
    --backdrop: #d6d6d6;
    --rule: #1a1a1a;
    --muted: #3a3a3a;
  }
  * { box-sizing: border-box; margin: 0; padding: 0; }
  html, body {
    width: 1200px; height: 988px; overflow: hidden;
    background: var(--backdrop);
    font-family: "Montserrat", sans-serif;
    color: var(--ink);
  }
  .stage {
    position: relative; width: 1200px; height: 988px;
    display: flex; align-items: center; justify-content: center; gap: 50px;
  }
  .card {
    position: relative; width: 530px; height: 304px;
    background: var(--paper);
    box-shadow: 0 6px 18px rgba(0,0,0,0.18);
    overflow: hidden;
  }
  .card-edge {
    position: absolute; left: 0; top: 0; bottom: 0; width: 10px;
    background: var(--ink);
  }
  .brand-name {
    font-weight: 700; font-size: 30px; letter-spacing: -0.5px;
    color: var(--ink); white-space: nowrap;
  }
  .card-front .brand-name {
    position: absolute; left: 0; right: 0; top: 50%;
    transform: translateY(-50%); text-align: center;
  }
  .rule { position: absolute; left: 0; right: 0; height: 2px; background: var(--rule); }
  .rule-top { top: 18px; }
  .rule-mid { top: 196px; }
  .rule-bottom { bottom: 18px; }
  .card-back .brand-name {
    position: absolute; left: 40px; top: 70px; font-size: 27px;
  }
  .contact-list {
    position: absolute; left: 40px; top: 130px;
    display: grid; grid-template-columns: 190px 230px; row-gap: 12px; column-gap: 14px;
    list-style: none;
  }
  .contact-item {
    display: flex; align-items: center; gap: 7px;
    font-size: 10.5px; color: var(--muted); white-space: nowrap;
  }
  .contact-icon { width: 13px; height: 13px; flex: none; }
  .person { position: absolute; left: 40px; top: 218px; }
  .person-name { font-size: 15px; font-weight: 500; letter-spacing: 1.5px; text-transform: uppercase; }
  .person-role { font-size: 10px; letter-spacing: 1.5px; text-transform: uppercase; color: var(--muted); margin-top: 5px; }
</style>
</head>
<body>
<main class="stage">
  <section class="card card-front" aria-label="Business card front">
    <div class="card-edge"></div>
    <div class="brand-name">Quarry Pharmacy Agents</div>
  </section>

  <section class="card card-back" aria-label="Business card back">
    <div class="card-edge"></div>
    <div class="rule rule-top"></div>
    <div class="brand-name">Quarry Pharmacy Agents</div>
    <ul class="contact-list">
      <li class="contact-item">
        <svg class="contact-icon" viewBox="0 0 14 14"><circle cx="7" cy="7" r="7" fill="#111"/><path d="M4.6 3.6l1.3 1.6-.7.9c.5 1 1.3 1.8 2.3 2.3l.9-.7 1.6 1.3-.8 1.2C6.7 10 4 7.3 3.4 4.4z" fill="#fff"/></svg>
        (03) 8417 3061
      </li>
      <li class="contact-item">
        <svg class="contact-icon" viewBox="0 0 14 14"><circle cx="7" cy="7" r="7" fill="#111"/><rect x="4" y="3.5" width="6" height="3" fill="#fff"/><rect x="3" y="6.5" width="8" height="3.5" rx=".6" fill="#fff"/><rect x="4.8" y="8.3" width="4.4" height="2.2" fill="#111"/></svg>
        (03) 8417 3062
      </li>
      <li class="contact-item">
        <svg class="contact-icon" viewBox="0 0 14 14"><circle cx="7" cy="7" r="7" fill="#111"/><rect x="3.3" y="4.3" width="7.4" height="5.4" fill="#fff"/><path d="M3.3 4.3L7 7.3l3.7-3" fill="none" stroke="#111" stroke-width=".8"/></svg>
        desk@quarryagents.com.au
      </li>
      <li class="contact-item">
        <svg class="contact-icon" viewBox="0 0 14 14"><circle cx="7" cy="7" r="7" fill="#111"/><circle cx="7" cy="7" r="3.6" fill="none" stroke="#fff" stroke-width=".8"/><path d="M3.4 7h7.2M7 3.4c-1.8 2-1.8 5.2 0 7.2M7 3.4c1.8 2 1.8 5.2 0 7.2" fill="none" stroke="#fff" stroke-width=".7"/></svg>
        www.quarryagents.com.au
      </li>
      <li class="contact-item" style="grid-column: 1 / span 2;">
        <svg class="contact-icon" viewBox="0 0 14 14"><circle cx="7" cy="7" r="7" fill="#111"/><path d="M7 11S4.2 7.9 4.2 6A2.8 2.8 0 0 1 9.8 6C9.8 7.9 7 11 7 11z" fill="#fff"/><circle cx="7" cy="6" r="1" fill="#111"/></svg>
        Level 18, 63 Harbour Road, Kew
      </li>
    </ul>
    <div class="rule rule-mid"></div>
    <div class="person">
      <div class="person-name">Graham Whitfield</div>
      <div class="person-role">Financial Advisor</div>
    </div>
    <div class="rule rule-bottom"></div>
  </section>
</main>
</body>
</html>
```